'Bright Ledger Hidden Keys' Book Cover

I need a professional book cover design for my new upcoming book that shows people how to get a high credit score.

Here are my two websites:

https://www.moneywordbank-lexa.info
https://moneywordbank-lexa.com/

I am looking for a clean, professional design that pops (emotional touch) and separates from the other books that are on the market. Cover aspect ratio 1:4 for Pagewisp version and 1:5 for the paperback version. Yellow or blue are good colors - but not must. See the basic examples that I provided. File delivery format PDF.

Book Title: Bright Ledger Hidden Keys
Byline: The Quick Lift And Mend Manual for Stellar Borrowing

Currently on Brindlecart pre-order:
https://www.brindlecart.example/Bright-Ledger-Hidden-Keys-Stellar-ebook/dp/Q48MPLRT71

I am the author of 36 published books on Brindlecart. My author profile is here:
brindlecart.example/author/gideonvarly

Targeted audience: People that want to improve or repair their bad credit score.

Target Market(s)

People/consumers in the US that want to improve or repair their credit score.

Industry/Entity Type

Consumer

Font styles to use
Sans Serif

Colors

Designer to choose colors to be used in the design.

Requirements
Must have
• Author name, Title, byline, and graphic element(s).
Nice to have
• - 2020 edition logo / batch

```html
<!DOCTYPE html>
<html lang="en">
<head>
<meta charset="utf-8">
<title>Bright Ledger Hidden Keys – Book Cover</title>
<link href="https://fonts.googleapis.com/css2?family=Bebas+Neue&family=Montserrat:wght@500;600;800&family=Nunito:wght@900&display=swap" rel="stylesheet">
<style>
  :root {
    --sky-light: #6ec0ee;
    --sky-mid: #3a93d6;
    --sky-deep: #1c6db8;
    --ink: #0f1d2e;
    --paper: #ffffff;
    --gauge-red: #d6401e;
    --gauge-orange: #f2a90a;
    --gauge-lime: #7ca51c;
    --gauge-green: #2e8a32;
    --label-orange: #f2a90a;
    --banner: #0b0b0b;
  }
  html, body {
    margin: 0;
    padding: 0;
    width: 800px;
    height: 1200px;
    overflow: hidden;
    background: var(--sky-deep);
  }
  .cover {
    position: relative;
    width: 800px;
    height: 1200px;
    overflow: hidden;
    background:
      radial-gradient(ellipse 60% 45% at 50% 55%, var(--sky-light) 0%, var(--sky-mid) 55%, var(--sky-deep) 100%);
    font-family: 'Montserrat', sans-serif;
    text-align: center;
  }
  .author {
    position: absolute;
    top: 50px;
    left: 0;
    width: 100%;
    margin: 0;
    font-family: 'Montserrat', sans-serif;
    font-weight: 600;
    font-size: 36px;
    line-height: 1;
    letter-spacing: 3px;
    color: var(--ink);
  }
  .title {
    margin: 0;
    font-family: 'Bebas Neue', sans-serif;
    font-weight: 400;
    color: var(--paper);
  }
  .title-line {
    position: absolute;
    left: 0;
    width: 100%;
    line-height: 1;
    letter-spacing: 1px;
    white-space: nowrap;
  }
  .title-line--first {
    top: 122px;
    font-size: 155px;
  }
  .title-line--second {
    top: 285px;
    font-size: 145px;
  }
  .byline {
    margin: 0;
    font-family: 'Montserrat', sans-serif;
    font-weight: 800;
    color: var(--ink);
  }
  .byline-lead,
  .byline-main {
    position: absolute;
    left: 0;
    width: 100%;
    line-height: 1;
    white-space: nowrap;
  }
  .byline-lead {
    top: 461px;
    font-size: 25px;
    letter-spacing: 0.5px;
  }
  .byline-main {
    top: 507px;
    font-size: 41px;
    letter-spacing: 1.5px;
  }
  .gauge-art {
    position: absolute;
    left: 82px;
    top: 604px;
    width: 640px;
    height: 320px;
    border-radius: 24px;
    background: linear-gradient(90deg, var(--gauge-red) 0%, var(--gauge-orange) 35%, var(--gauge-lime) 65%, var(--gauge-green) 100%);
    opacity: 0.85;
  }
  .gauge-label {
    position: absolute;
    top: 938px;
    margin: 0;
    font-family: 'Nunito', sans-serif;
    font-weight: 900;
    font-size: 42px;
    line-height: 1;
    letter-spacing: 1px;
  }
  .gauge-label--poor { left: 90px; color: var(--gauge-red); }
  .gauge-label--good { left: 584px; color: var(--label-orange); }
  .series-banner {
    position: absolute;
    left: 74px;
    top: 1122px;
    width: 654px;
    height: 48px;
    background: var(--banner);
    color: var(--paper);
    font-family: 'Montserrat', sans-serif;
    font-weight: 500;
    font-size: 29px;
    letter-spacing: 1px;
    line-height: 48px;
    white-space: nowrap;
  }
</style>
</head>
<body>
  <main class="cover">
    <p class="author">GIDEON VARLY</p>

    <h1 class="title">
      <span class="title-line title-line--first">BRIGHT LEDGER</span>
      <span class="title-line title-line--second">HIDDEN KEYS</span>
    </h1>

    <h2 class="byline">
      <span class="byline-lead">THE QUICK LIFT &amp; MEND MANUAL FOR</span>
      <span class="byline-main">STELLAR BORROWING</span>
    </h2>

    <div class="gauge-art" role="img" aria-label="Illustration of a credit score gauge in red, orange and green bands with a white needle pointing toward good"></div>

    <p class="gauge-label gauge-label--poor">POOR</p>
    <p class="gauge-label gauge-label--good">GOOD</p>

    <div class="series-banner">VARLY FINANCIAL LITERACY PROGRAM</div>
  </main>
</body>
</html>
```